New Update: I am changing the title of the book and the back cover text. Title was too long before. Same style as before.
New Title: Under the Quiet Sky
New Subtitle: A Gardener’s Notes on Patience (italics on front cover)

Back cover text:
Under the Quiet Sky: A Gardener’s Notes on Patience offers clear, compassionate guidance for those recovering from total loss. Drawing from his experience as a Brennick Flood survivor, Tobias Quellhorst shares practical advice on insurance, rebuilding, and emotional healing, along with lessons in strength and community. This is not a book about tragedy; it’s about perseverance and renewal. Under the Quiet Sky is a trusted companion for anyone rebuilding life, home, and hope after disaster.

Font styles to use
Serif

Colors
EB3D1F
EC4F4E
F09395
F8D3D4
FCEDEE

Requirements
Should not have
• No pictures or anything related to fire on the cover.

```html
<!DOCTYPE html>
<html lang="en">
<head>
<meta charset="utf-8">
<title>Under the Quiet Sky – Front Cover</title>
<link rel="stylesheet" href="https://fonts.googleapis.com/css2?family=Oranienbaum&family=Source+Serif+4:ital,opsz,wght@0,8..60,400;1,8..60,400&family=Oswald:wght@600&display=swap">
<style>
  :root {
    --backdrop: #c6c6c6;
    --cover-glow: #d44d24;
    --cover-mid: #8a1a16;
    --cover-deep: #4e0a0b;
    --ink-cream: #fbf1e1;
    --emblem-tone: #f6ece6;
  }
  * { margin: 0; padding: 0; box-sizing: border-box; }
  html, body {
    width: 1200px; height: 696px; overflow: hidden;
    background: var(--backdrop);
  }
  .stage {
    width: 1200px; height: 696px;
    display: flex; align-items: center; justify-content: center;
  }
  .front-cover {
    position: relative;
    width: 413px; height: 620px;
    background:
      radial-gradient(ellipse 60% 42% at 50% 38%, var(--cover-glow) 0%, rgba(180,55,30,0.55) 40%, rgba(138,26,22,0) 75%),
      radial-gradient(ellipse 95% 85% at 50% 45%, var(--cover-mid) 0%, #6e1212 60%, var(--cover-deep) 100%);
    box-shadow: 0 14px 18px -10px rgba(0,0,0,0.45);
    color: var(--ink-cream);
    text-align: center;
  }
  .book-title {
    position: absolute; top: 46px; left: 0; right: 0;
    font-family: "Oranienbaum", serif;
    font-weight: 400;
    font-size: 62px;
    letter-spacing: 1px;
    text-transform: uppercase;
    white-space: nowrap;
  }
  .book-title span {
    display: block;
    height: 88px;
    line-height: 88px;
    transform: scaleY(1.5);
    transform-origin: 50% 50%;
  }
  .series-line {
    position: absolute; top: 318px; left: 0; right: 0;
    font-family: "Source Serif 4", serif;
    font-size: 21px;
    line-height: 26px;
  }
  .cover-emblem {
    position: absolute; top: 364px; left: 50%;
    width: 108px; height: 128px; transform: translateX(-50%);
    border-radius: 50% 50% 46% 46% / 55% 55% 45% 45%;
    background: radial-gradient(ellipse at 50% 60%, var(--emblem-tone) 0%, rgba(246,236,230,0.8) 55%, rgba(246,236,230,0.15) 100%);
  }
  .book-subtitle {
    position: absolute; top: 502px; left: 0; right: 0;
    font-family: "Source Serif 4", serif;
    font-style: italic;
    font-size: 19px;
    line-height: 24px;
  }
  .author-name {
    position: absolute; top: 560px; left: 0; right: 0;
    font-family: "Oswald", sans-serif;
    font-weight: 600;
    font-size: 21px;
    line-height: 30px;
    letter-spacing: 3.5px;
    text-transform: uppercase;
  }
</style>
</head>
<body>
  <main class="stage">
    <article class="front-cover">
      <h1 class="book-title"><span>Under the</span><span>Quiet</span><span>Sky</span></h1>
      <p class="series-line">A Survivor’s Story</p>
      <div class="cover-emblem" role="img" aria-label="Cover emblem artwork"></div>
      <p class="book-subtitle">A Gardener’s Notes<br>on Patience</p>
      <p class="author-name">Tobias Quellhorst</p>
    </article>
  </main>
</body>
</html>
```